NEW FACEBOOK AD CREATIVES FOR MARKETING AGENCY

We need one single static image AND a Carousel Ad Design With 5 Cards Total in it.

We advertise a SaaS Product that teaches businesses how to use incentive based marketing to get more sales and leads.

Using our service businesses can give away smart devices like smartwatches, earpods, mp4 players, tablets, etc. as a gift bonus along with their product or service as an added value benefit to help them create more attractive offers and to get more sales.

I have attached two designs that get me my best results on facebook ads so far so I want to create something very similar with a different look and showcasing 3-4 of the items I have attached images for.

CONTENT & INSTRUCTIONS:
MAIN TEXT: TRIPLE YOUR SALES OFFERING FREE SMART DEVICES AS A BONUS FOR BUYING YOUR PRODUCT OR SERVICE

Target Market(s)

ENTREPRENEURS, INVESTORS, BUSINESS OWNERS, MEDIA AGENCIES, BROKERAGES

Industry/Entity Type

marketing gifting

Requirements
Must have
• must match color scheme of website www.brightlooprewardhub.biz as this is where they will be redirected to when they click.
Nice to have
• the ads must be 1080x1080 Static newsfeed ad and carousel ads

```html
<!DOCTYPE html>
<html lang="en">
<head>
<meta charset="utf-8">
<title>Triple Your Sales – Free Smart Devices</title>
<link rel="stylesheet" href="https://fonts.googleapis.com/css2?family=Bebas+Neue&family=Montserrat:ital,wght@0,500;0,700;0,800;0,900;1,600;1,900&display=swap">
<style>
  :root {
    --orange-light: #ffa200;
    --orange: #ff7a0c;
    --orange-deep: #ff6200;
    --sky-deep: #14a8ec;
    --sky: #2ec9f6;
    --sky-pale: #d2f8ff;
    --royal: #1356c4;
    --gold: #f5b800;
    --ink: #111111;
    --grey: #555a60;
    --white: #ffffff;
  }
  * { margin: 0; padding: 0; box-sizing: border-box; }
  html, body { width: 1200px; height: 1200px; overflow: hidden; background: var(--white); }
  .ad {
    position: relative;
    width: 1200px;
    height: 1200px;
    overflow: hidden;
    background: radial-gradient(ellipse at 65% 62%, var(--sky-pale) 0%, var(--sky) 48%, var(--sky-deep) 100%);
    font-family: "Montserrat", sans-serif;
  }
  .ad__shapes { position: absolute; inset: 0; }

  .headline {
    position: absolute;
    font-family: "Bebas Neue", sans-serif;
    font-weight: 400;
    color: var(--white);
    line-height: 1;
    white-space: nowrap;
  }
  .headline--lead { left: 104px; top: 72px; font-size: 126px; letter-spacing: 1px; }
  .headline--big { left: 638px; top: 46px; font-size: 232px; letter-spacing: 2px; }

  .product {
    position: absolute;
    border-radius: 28px;
    box-shadow: 0 14px 30px rgba(0, 50, 90, .18);
  }
  .product--player {
    left: 30px; top: 399px; width: 268px; height: 186px;
    background: linear-gradient(155deg, #3d55a8 0%, #0e1526 55%, #1d5fc8 100%);
  }
  .product--earbuds {
    left: 322px; top: 377px; width: 236px; height: 246px;
    background: linear-gradient(160deg, #2a5aa6 0%, #101a2c 50%, #b98d4c 100%);
  }
  .product--watch {
    left: 589px; top: 390px; width: 221px; height: 246px;
    border-radius: 110px;
    background: linear-gradient(160deg, #3b4452 0%, #15191f 70%, #e79a20 100%);
  }
  .product--headphones {
    left: 852px; top: 390px; width: 284px; height: 310px;
    background: linear-gradient(165deg, #2d2d2d 0%, #0b0b0b 60%, #9b7643 100%);
  }
  .product--speaker {
    left: 127px; top: 712px; width: 424px; height: 208px;
    border-radius: 100px;
    background: linear-gradient(180deg, #4c586b 0%, #2b3545 55%, #1a202b 100%);
  }

  .offer-tag {
    position: absolute;
    left: 615px; top: 730px;
    width: 46px; height: 178px;
    background: var(--gold);
    display: flex; align-items: center; justify-content: center;
  }
  .offer-tag span {
    display: block;
    transform: rotate(90deg);
    font-weight: 800;
    font-size: 25px;
    letter-spacing: 1px;
    color: var(--ink);
    white-space: nowrap;
  }
  .offer-free {
    position: absolute;
    left: 665px; top: 705px;
    font-weight: 900;
    font-size: 170px;
    letter-spacing: -6px;
    line-height: 1;
    color: var(--royal);
  }
  .offer-bar {
    position: absolute;
    left: 670px; top: 852px;
    width: 444px; height: 56px;
    background: var(--orange);
    display: flex; align-items: center; justify-content: center;
    color: var(--white);
    font-weight: 800;
    font-size: 41px;
    letter-spacing: .5px;
  }
  .offer-note {
    position: absolute;
    left: 664px; top: 918px;
    font-style: italic;
    font-weight: 600;
    font-size: 36px;
    line-height: 43px;
    color: var(--ink);
    white-space: nowrap;
  }
  .offer-note strong { font-weight: 900; }

  .brand {
    position: absolute;
    left: 50px; top: 1070px;
    display: flex; align-items: center; gap: 16px;
  }
  .brand__dot { width: 32px; height: 32px; border-radius: 50%; background: var(--royal); flex: none; }
  .brand__name {
    font-weight: 800;
    font-size: 32px;
    line-height: 38px;
    color: var(--royal);
    text-transform: uppercase;
    letter-spacing: .5px;
  }
  .site {
    position: absolute;
    left: 540px; top: 1124px;
    font-size: 28px;
    font-weight: 500;
    color: var(--grey);
    white-space: nowrap;
  }
  .site b { font-weight: 700; color: var(--royal); }
</style>
</head>
<body>
<main class="ad">
  <svg class="ad__shapes" viewBox="0 0 1200 1200" width="1200" height="1200" aria-hidden="true">
    <defs>
      <linearGradient id="band-orange" x1="0" y1="0" x2="1" y2="0">
        <stop offset="0" stop-color="#ffa200"/>
        <stop offset="0.55" stop-color="#ff7a0c"/>
        <stop offset="1" stop-color="#ff6200"/>
      </linearGradient>
    </defs>
    <path d="M0 0 H1200 V76 C1172 200 1125 330 1045 356 C995 370 950 368 905 360 L0 170 Z" fill="url(#band-orange)"/>
    <path d="M0 195 L900 372 C950 381 1010 384 1072 362" fill="none" stroke="#ffffff" stroke-width="2.5"/>
    <path d="M1165 0 C1150 150 1125 300 1060 360" fill="none" stroke="#ffffff" stroke-width="2"/>
    <path d="M0 958 C60 935 100 928 160 928 C230 930 300 945 380 962 L1200 1115 V1200 H0 Z" fill="#ffffff"/>
  </svg>

  <h1 class="headline headline--lead">TRIPLE YOUR</h1>
  <div class="headline headline--big">SALES</div>

  <div class="product product--player" role="img" aria-label="Photo of a slim MP4 media player"></div>
  <div class="product product--earbuds" role="img" aria-label="Photo of wireless earbuds in an open charging case"></div>
  <div class="product product--watch" role="img" aria-label="Photo of a round black smartwatch"></div>
  <div class="product product--headphones" role="img" aria-label="Photo of black and gold wireless headphones shown from three angles"></div>
  <div class="product product--speaker" role="img" aria-label="Photo of a portable cylindrical bluetooth speaker"></div>

  <div class="offer-tag"><span>OFFERING</span></div>
  <div class="offer-free">FREE</div>
  <div class="offer-bar">SMART DEVICES</div>
  <p class="offer-note">As a bonus for <strong>Buying</strong><br>Your Product or <strong>Service</strong></p>

  <div class="brand">
    <span class="brand__dot"></span>
    <span class="brand__name">BrightLoop<br>Reward Hub</span>
  </div>
  <div class="site">www.<b>brightlooprewardhub</b>.biz</div>
</main>
</body>
</html>
```